PENNIMARTEL & PENNIMARTEL,LLP NEEDS A NEW LETTERHEAD DESIGN

a conservative yet contemporary layout befitting a long established
firm, consistent with the times, some form of logo so it catches ones attention, and is
admirable, but portrays integrity
Updates

I would like to approve #22066987 Please advise how to do this as it’s confusing on the site so I can approve payment for the designer

Target Market(s)

real estate investors and building management people

Industry/Entity Type

Law Firm

Font styles to use
Serif

Colors

Designer to choose colors to be used in the design.

Requirements
Must have
• some form of conservative logo

```html
<!DOCTYPE html>
<html lang="en">
<head>
<meta charset="utf-8">
<title>Pennimartel &amp; Pennimartel, LLP — Letterhead</title>
<link rel="stylesheet" href="https://fonts.googleapis.com/css2?family=Cinzel:wght@500&family=Roboto:wght@400;500&display=swap">
<style>
  :root {
    --backdrop: #d4d4d4;
    --paper: #ffffff;
    --navy: #1f4f8b;
    --slate: #6b6b6b;
    --ink-soft: #555b63;
    --rule: #8a8a8a;
  }
  * { box-sizing: border-box; margin: 0; padding: 0; }
  html, body { width: 1200px; height: 922px; overflow: hidden; }
  body {
    background: var(--backdrop);
    display: flex;
    align-items: center;
    justify-content: center;
  }
  .letterhead {
    position: relative;
    width: 660px;
    height: 854px;
    background: linear-gradient(160deg, #ffffff 0%, #f6f6f6 100%);
    box-shadow: 0 10px 30px rgba(0,0,0,0.12);
  }
  .masthead {
    position: absolute;
    top: 58px;
    left: 52px;
    display: flex;
    align-items: center;
  }
  .brand-square {
    width: 50px;
    height: 50px;
    background: var(--navy);
  }
  .brand-divider {
    width: 1px;
    height: 76px;
    background: var(--rule);
    margin: 0 14px 0 16px;
  }
  .brand-name {
    font-family: "Cinzel", "Times New Roman", serif;
    font-weight: 500;
    color: var(--navy);
    line-height: 1.05;
  }
  .brand-name .line { display: block; font-size: 21px; letter-spacing: 0.3px; }
  .brand-name .line-second { padding-left: 2px; }
  .brand-name .brand-rule {
    display: block;
    width: 104px;
    height: 1px;
    background: var(--navy);
    margin: 6px 0 0 2px;
  }
  .brand-name .suffix {
    display: block;
    font-size: 11px;
    text-align: right;
    width: 140px;
    margin-top: -5px;
  }
  .footer {
    position: absolute;
    left: 52px;
    top: 722px;
    display: flex;
    gap: 46px;
    font-family: "Roboto", Arial, sans-serif;
    font-size: 10.5px;
    color: var(--ink-soft);
    line-height: 1.45;
  }
  .firm-block .firm-name { color: var(--navy); font-weight: 500; }
  .contact-list { list-style: none; padding-top: 14px; }
  .contact-list li { display: flex; align-items: center; gap: 5px; }
  .contact-list svg { width: 9px; height: 9px; fill: var(--navy); }
  .web-band {
    position: absolute;
    right: 8px;
    top: 786px;
    width: 248px;
    height: 36px;
    background: var(--navy);
    color: #ffffff;
    font-family: "Roboto", Arial, sans-serif;
    font-size: 11.5px;
    letter-spacing: 1px;
    display: flex;
    align-items: center;
    justify-content: center;
  }
</style>
</head>
<body>
  <main class="letterhead">
    <header class="masthead">
      <div class="brand-square" aria-hidden="true"></div>
      <div class="brand-divider" aria-hidden="true"></div>
      <div class="brand-name">
        <span class="line">Pennimartel</span>
        <span class="line line-second">&amp; Pennimartel</span>
        <span class="brand-rule" aria-hidden="true"></span>
        <span class="suffix">LLP</span>
      </div>
    </header>

    <footer class="footer">
      <address class="firm-block" style="font-style: normal;">
        <div class="firm-name">Pennimartel &amp; Pennimartel, LLP</div>
        <div>418 Harbor Avenue Suite 210</div>
        <div>Brooklyn, New York 11201</div>
      </address>
      <ul class="contact-list">
        <li>
          <svg viewBox="0 0 10 10" aria-hidden="true"><path d="M2 0.5 L3.6 0.5 L4.2 3 L3 3.8 C3.6 5.2 4.8 6.4 6.2 7 L7 5.8 L9.5 6.4 L9.5 8 C9.5 9 8.8 9.5 8 9.5 C4 9.2 0.8 6 0.5 2 C0.5 1.2 1 0.5 2 0.5 Z"/></svg>
          (718) 555-0143
        </li>
        <li>
          <svg viewBox="0 0 10 10" aria-hidden="true"><rect x="2.5" y="0.5" width="5" height="3"/><rect x="0.5" y="3.5" width="9" height="4" rx="1"/><rect x="2.5" y="7" width="5" height="2.5"/></svg>
          (718)-555-0178
        </li>
        <li>
          <svg viewBox="0 0 10 10" aria-hidden="true"><path d="M0.5 2 H9.5 V8.5 H0.5 Z M1.4 2.8 V7.7 H8.6 V2.8 L5 5.6 Z" fill-rule="evenodd"/></svg>
          info@pplawfirm.com
        </li>
      </ul>
    </footer>

    <div class="web-band">www.pennimartellaw.com</div>
  </main>
</body>
</html>
```